2026 Kelvar Montra medium roof

Van montra logo wrap, construction company Bright Oak Renovations LLC

Target Market(s)

More customers

Industry/Entity Type

License contractor, remodeling, construction

Colors

Designer to choose colors to be used in the design.

Requirements
Must have
• House logo, jobs I offer, phone number,, license & insured , KLR acquitted business,
Nice to have
• I would like to have the KLR logo in lower right bottom of van

```html
<!DOCTYPE html>
<html lang="en">
<head>
<meta charset="utf-8">
<title>Bright Oak Renovations LLC – Kelvar Montra Van Wrap</title>
<link rel="stylesheet" href="https://fonts.googleapis.com/css2?family=Open+Sans:wght@400;600;700&display=swap">
<style>
  :root {
    --navy: #163a63;
    --steel: #6d7f95;
    --panel: #e6e9ee;
    --white: #ffffff;
    --glass: #2a2f36;
    --trim: #2b2e33;
    --tyre: #1e1f22;
    --rim: #b9bec5;
    --taillight: #c8202a;
    --ground: #f2f3f5;
  }
  html, body {
    margin: 0;
    padding: 0;
    width: 1200px;
    height: 543px;
    overflow: hidden;
    background: var(--ground);
  }
  .van-wrap {
    display: block;
    width: 1200px;
    height: 543px;
    font-family: "Open Sans", Arial, sans-serif;
  }
  .body-base { fill: var(--navy); }
  .side-panel { fill: var(--panel); }
  .accent-band { fill: var(--steel); }
  .window { fill: var(--glass); }
  .lower-trim { fill: var(--trim); }
  .tyre { fill: var(--tyre); }
  .rim { fill: var(--rim); }
  .tail-light { fill: var(--taillight); }
  .head-light { fill: #3c4a5c; }
  .brand-mark { fill: var(--navy); }
  .accreditation-badge { fill: var(--white); stroke: var(--navy); stroke-width: 2; }
  .accreditation-badge-inner { fill: var(--navy); }
  .banner { fill: var(--navy); }

  .brand-name { fill: var(--navy); font-weight: 700; }
  .banner-url { fill: var(--white); font-weight: 600; letter-spacing: 1.6px; }
  .trust-line { fill: var(--navy); font-weight: 700; letter-spacing: 0.6px; }
  .accredited-heading { fill: var(--navy); font-weight: 700; }
  .services-title { fill: var(--white); font-weight: 600; }
  .service-item { fill: var(--white); font-weight: 400; }
  .phone-number { fill: var(--white); font-weight: 700; }
  .phone-icon { fill: none; stroke: var(--steel); stroke-width: 1.6; }
  .license-note { fill: var(--navy); font-size: 8px; }
  .license-note .label { font-weight: 700; }
</style>
</head>
<body>
<svg class="van-wrap" viewBox="0 0 1200 543" xmlns="http://www.w3.org/2000/svg">
  <defs>
    <clipPath id="van-body">
      <path d="M64 400 L58 360 Q60 322 92 300 L188 262 Q220 160 300 100 Q360 62 470 60 L1080 56 Q1132 60 1140 110 L1146 410 Q1146 430 1130 432 L70 432 Z"/>
    </clipPath>
  </defs>

  <!-- Van body and wrap -->
  <g class="van-body" clip-path="url(#van-body)">
    <rect class="body-base" x="0" y="0" width="1200" height="543"/>
    <path class="accent-band" d="M585 50 Q420 150 372 380 L385 445 L770 445 C860 350 960 270 960 150 Q955 80 930 50 Z"/>
    <path class="side-panel" d="M605 50 Q445 150 390 380 L402 445 L700 445 C800 360 935 270 935 150 Q930 80 895 50 Z"
          role="img" aria-label="Light grey panel with a faint line pattern of hand tools"/>
    <rect class="lower-trim" x="460" y="372" width="300" height="42" rx="2"/>
    <rect class="lower-trim" x="60" y="372" width="110" height="60"/>
    <rect class="lower-trim" x="845" y="372" width="301" height="42"/>
    <rect class="tail-light" x="1110" y="248" width="26" height="112" rx="6"/>
    <path class="head-light" d="M88 300 L150 282 Q150 312 132 326 L92 330 Z"/>
  </g>

  <!-- Cab window -->
  <path class="window" d="M248 150 Q300 138 430 134 Q440 136 438 150 L428 268 L280 272 L195 280 Q215 190 248 150 Z"/>

  <!-- Wheels -->
  <g class="wheels">
    <circle class="tyre" cx="222" cy="455" r="56"/>
    <circle class="rim" cx="222" cy="455" r="34"/>
    <circle class="tyre" cx="935" cy="455" r="56"/>
    <circle class="rim" cx="935" cy="455" r="34"/>
  </g>

  <!-- Phone -->
  <g class="phone-block">
    <circle class="phone-icon" cx="162" cy="322" r="12"/>
    <path class="phone-icon" d="M157 316 q-2 6 4 12 q6 5 10 3" />
    <text class="phone-number" x="180" y="330" font-size="21">(555) 318-0462</text>
  </g>

  <!-- Brand -->
  <rect class="brand-mark" x="598" y="120" width="84" height="84"/>
  <text class="brand-name" x="640" y="281" font-size="31" text-anchor="middle">BRIGHT OAK</text>
  <text class="brand-name" x="640" y="302" font-size="22" text-anchor="middle">RENOVATIONS LLC</text>

  <path class="banner" d="M443 310 L832 310 L818 322 L832 336 L443 336 L457 322 Z"/>
  <text class="banner-url" x="640" y="328" font-size="15" text-anchor="middle">BRIGHTOAKRENOVATIONS.COM</text>

  <text class="trust-line" x="640" y="354" font-size="17" text-anchor="middle">LICENSED · INSURED · TRUSTED</text>

  <text class="license-note" x="640" y="431" text-anchor="middle"><tspan class="label">License #:</tspan> 241900386</text>

  <!-- Accreditation -->
  <text class="accredited-heading" x="820" y="124" font-size="16" text-anchor="middle">PROUD TO BE</text>
  <text class="accredited-heading" x="820" y="143" font-size="16" text-anchor="middle">ACCREDITED</text>
  <rect class="accreditation-badge" x="791" y="162" width="56" height="94" rx="4"/>
  <rect class="accreditation-badge-inner" x="799" y="172" width="40" height="74" rx="2"/>

  <!-- Services -->
  <text class="services-title" x="1091" y="97" font-size="25" text-anchor="end">SERVICES</text>
  <g class="service-list" font-size="13" text-anchor="end">
    <text class="service-item" x="1092" y="143">• Drywall &amp; Painting</text>
    <text class="service-item" x="1092" y="175">• Interior &amp; Exterior</text>
    <text class="service-item" x="1092" y="205">• Siding  • Roofing</text>
    <text class="service-item" x="1092" y="236">• Doors &amp; Windows</text>
    <text class="service-item" x="1092" y="265">• Plumbing &amp; Electrical</text>
    <text class="service-item" x="1092" y="297">• Kitchens &amp; Bathrooms</text>
    <text class="service-item" x="1092" y="327">• Flooring • Decks • Fences</text>
  </g>
</svg>
</body>
</html>
```